Corwell Facilities Services Business Card.

We need a card for Corwell Facilities Services with a new look. We also have service and supply partners that we would like to have on the card. Lumacoat is a surface application company, Corwell Facilities is a facilities services business, Tavish Supply Co is a Facilities supply business, Pelvra is a product that we use that powers our business.

```html
<!DOCTYPE html>
<html lang="en">
<head>
<meta charset="utf-8">
<title>Corwell Facilities Services Business Card</title>
<link href="https://fonts.googleapis.com/css2?family=Montserrat:wght@500;700;800&family=Arimo:wght@400&display=swap" rel="stylesheet">
<style>
  :root {
    --bg: #c9c9c9;
    --green: #3db64a;
    --teal: #21988a;
    --blue: #1172c0;
    --navy: #0d2a55;
    --ink: #2a2a2a;
    --mist-blue: #e4eff8;
    --mist-green: #eef6ee;
    --white: #ffffff;
  }
  * { margin: 0; padding: 0; box-sizing: border-box; }
  html, body { width: 1200px; height: 900px; overflow: hidden; }
  body {
    background: var(--bg);
    font-family: "Arimo", Arial, sans-serif;
    position: relative;
  }
  .card {
    position: absolute;
    left: 290px;
    width: 620px;
    height: 354px;
    border-radius: 26px;
    overflow: hidden;
    box-shadow: 0 6px 14px rgba(0,0,0,.25);
  }
  .card--front {
    top: 70px;
    background: linear-gradient(200deg, var(--green) 0%, var(--teal) 48%, var(--blue) 100%);
  }
  .card--back { top: 470px; background: var(--white); }

  .decor { position: absolute; border-radius: 50%; }
  .front-decor {
    width: 300px; height: 300px; right: -40px; top: 20px;
    background: rgba(17,114,192,.22);
  }
  .back-decor-blue {
    width: 330px; height: 330px; right: -30px; top: -40px;
    background: var(--mist-blue);
  }
  .back-decor-green {
    width: 230px; height: 230px; right: -40px; top: 170px;
    background: var(--mist-green);
  }

  .brand {
    position: absolute;
    font-family: "Montserrat", sans-serif;
    font-weight: 800;
    line-height: 1;
  }
  .brand__name { display: block; }
  .brand__sub { display: block; }
  .brand--front {
    color: var(--white);
    left: 140px; top: 120px;
  }
  .brand--front .brand__name { font-size: 72px; letter-spacing: -1px; }
  .brand--front .brand__sub { font-size: 27px; margin-top: 4px; }
  .brand--back {
    color: var(--blue);
    left: 48px; top: 70px;
  }
  .brand--back .brand__name { font-size: 64px; letter-spacing: -1px; }
  .brand--back .brand__sub { font-size: 24px; margin-top: 4px; }

  .contact { position: absolute; left: 48px; top: 212px; color: var(--ink); }
  .contact__name {
    font-family: "Montserrat", sans-serif; font-weight: 800;
    font-size: 24px; color: var(--blue);
  }
  .contact__title { font-size: 17px; margin-bottom: 10px; }
  .contact__row { display: flex; align-items: center; gap: 10px; font-size: 17px; line-height: 1.4; }
  .contact__row svg { width: 16px; height: 16px; flex: none; }
  .accent { color: var(--blue); }

  .partners {
    position: absolute; right: 34px; top: 46px;
    width: 230px; text-align: center;
    font-family: "Montserrat", sans-serif;
  }
  .partner { font-weight: 800; display: flex; align-items: center; justify-content: center; gap: 8px; }
  .partner--lumacoat { font-size: 26px; color: var(--blue); margin-bottom: 12px; }
  .partner--tavish { font-size: 20px; color: var(--blue); margin-bottom: 14px; }
  .partner__dot { width: 22px; height: 22px; border-radius: 50%; background: var(--blue); }
  .powered { font-size: 12px; font-weight: 500; color: var(--navy); }
  .partner--pelvra { font-size: 30px; color: var(--navy); letter-spacing: 1px; }
  .address {
    margin-top: 22px; font-family: "Arimo", Arial, sans-serif;
    font-size: 17px; line-height: 1.3; color: var(--ink);
  }
</style>
</head>
<body>

<section class="card card--front" aria-label="Card front">
  <div class="decor front-decor"></div>
  <div class="brand brand--front">
    <span class="brand__name">Corwell</span>
    <span class="brand__sub">Facilities Services</span>
  </div>
</section>

<section class="card card--back" aria-label="Card back">
  <div class="decor back-decor-blue"></div>
  <div class="decor back-decor-green"></div>

  <div class="brand brand--back">
    <span class="brand__name">Corwell</span>
    <span class="brand__sub">Facilities Services</span>
  </div>

  <div class="contact">
    <p class="contact__name">Daniel Marsh</p>
    <p class="contact__title">Managing Director</p>
    <p class="contact__row">
      <svg viewBox="0 0 16 16"><rect x="1" y="1" width="14" height="14" rx="2" fill="none" stroke="#1172c0" stroke-width="1.5"/><path d="M5 4c0 4 3 7 7 7l0-2-2-.5-1 1c-1-.5-2-1.5-2.5-2.5l1-1L7 4z" fill="#1172c0"/></svg>
      044-555 018 274
    </p>
    <p class="contact__row">
      <svg viewBox="0 0 16 16"><rect x="1" y="3" width="14" height="10" fill="#1172c0"/><path d="M1 3l7 6 7-6" fill="none" stroke="#fff" stroke-width="1.3"/></svg>
      info@corwellfs.com
    </p>
    <p class="contact__row">
      <svg viewBox="0 0 16 16"><circle cx="8" cy="8" r="7" fill="none" stroke="#1172c0" stroke-width="1.5"/><path d="M1 8h14M8 1c-3 4-3 10 0 14M8 1c3 4 3 10 0 14" fill="none" stroke="#1172c0" stroke-width="1.2"/></svg>
      <span>www.<span class="accent">corwellfs</span>.com</span>
    </p>
  </div>

  <div class="partners">
    <p class="partner partner--lumacoat">Lumacoat</p>
    <p class="partner partner--tavish"><span class="partner__dot"></span>Tavish Supply Co</p>
    <p class="powered">Powered by</p>
    <p class="partner partner--pelvra">Pelvra</p>
    <p class="address">118, Harlow Street<br>Brenton, 40217</p>
  </div>
</section>

</body>
</html>
```